Granite, Zinc and Clay Roofing LLC needs a new business card

I need a new business card because I have a new address.
I do slate copper and tile roofs. My webpage is: www.granitezincandclayroofing.example

```html
<!DOCTYPE html>
<html lang="en">
<head>
<meta charset="utf-8">
<title>Granite, Zinc and Clay Roofing LLC – Business Card</title>
<link rel="stylesheet" href="https://fonts.googleapis.com/css2?family=Arimo:wght@400&family=Tinos:wght@400;700&display=swap">
<style>
  :root {
    --page-bg: #2a2a2c;
    --card-blue: #4f9ccb;
    --pattern-blue: #5aa6d4;
    --ink: #0b0b0c;
    --rule: #27465c;
  }
  * { margin: 0; padding: 0; box-sizing: border-box; }
  html, body {
    width: 1200px; height: 1108px; overflow: hidden;
    background: var(--page-bg);
  }
  .sheet {
    position: relative; width: 1200px; height: 1108px;
  }
  .card {
    position: absolute; top: 186px;
    width: 420px; height: 735px;
    background: var(--card-blue);
    border-radius: 24px;
    overflow: hidden;
    color: var(--ink);
    text-align: center;
  }
  .card--front { left: 150px; }
  .card--back { left: 630px; }

  .wordmark {
    font-family: "Tinos", serif;
    font-weight: 400;
    color: var(--ink);
    line-height: 1.15;
  }
  .card--front .wordmark {
    position: absolute; top: 120px; left: 40px; right: 40px;
    font-size: 34px;
    display: flex; flex-direction: column; align-items: center; gap: 14px;
  }
  .wordmark__square {
    width: 26px; height: 26px; background: var(--ink);
  }

  .person {
    position: absolute; top: 385px; left: 0; right: 0;
  }
  .person__name {
    font-family: "Tinos", serif; font-weight: 700; font-size: 30px;
  }
  .person__role {
    font-family: "Arimo", sans-serif; font-size: 19px; margin-top: 2px;
  }
  .icon-row {
    display: flex; align-items: center; justify-content: center;
    gap: 8px; margin: 14px 40px 0;
  }
  .icon-row__rule { flex: 1; height: 1px; background: var(--rule); }
  .icon {
    width: 30px; height: 30px; background: var(--ink); border-radius: 5px;
    display: flex; align-items: center; justify-content: center;
  }
  .contact {
    font-family: "Arimo", sans-serif; font-size: 18px; line-height: 1.35;
    margin-top: 12px;
  }
  .divider {
    width: 300px; height: 1px; background: var(--rule);
    margin: 18px auto 0;
  }
  .address {
    font-family: "Arimo", sans-serif; font-size: 19px; line-height: 1.35;
    margin-top: 22px;
  }

  .back-pattern {
    position: absolute; inset: 0;
    background: linear-gradient(160deg, var(--pattern-blue), var(--card-blue) 60%);
  }
  .card--back .wordmark {
    position: absolute; top: 470px; left: 60px; right: 60px;
    font-size: 22px;
  }
</style>
</head>
<body>
<main class="sheet">
  <section class="card card--front">
    <div class="wordmark">
      <span class="wordmark__square"></span>
      <span>Granite, Zinc and Clay Roofing LLC</span>
    </div>

    <div class="person">
      <div class="person__name">Laszlo (Lou) Varga</div>
      <div class="person__role">Owner</div>

      <div class="icon-row">
        <span class="icon-row__rule"></span>
        <span class="icon" aria-label="Phone">
          <svg width="18" height="18" viewBox="0 0 24 24"><path fill="none" stroke="#4f9ccb" stroke-width="2" d="M6 3l3 4-2 2c1 3 4 6 7 7l2-2 4 3-2 3C10 20 4 14 3 6z"/></svg>
        </span>
        <span class="icon" aria-label="Web">
          <svg width="18" height="18" viewBox="0 0 24 24" fill="none" stroke="#4f9ccb" stroke-width="2"><circle cx="12" cy="12" r="9"/><path d="M3 12h18M12 3c3 3 3 15 0 18M12 3c-3 3-3 15 0 18"/></svg>
        </span>
        <span class="icon" aria-label="Email">
          <svg width="18" height="18" viewBox="0 0 24 24" fill="none" stroke="#4f9ccb" stroke-width="2"><rect x="3" y="6" width="18" height="12"/><path d="M3 6l9 7 9-7"/></svg>
        </span>
        <span class="icon-row__rule"></span>
      </div>

      <div class="contact">
        <div>(555)014-2876</div>
        <div>www.granitezincandclayroofing.example</div>
        <div>gzcroofing@example.com</div>
      </div>

      <div class="divider"></div>

      <div class="address">
        <div>2870 Millbrook Rd</div>
        <div>Fairview, OH 44000</div>
      </div>
    </div>
  </section>

  <section class="card card--back">
    <div class="back-pattern" role="img" aria-label="Repeating embossed pattern of the company emblem in tonal blue"></div>
    <div class="wordmark">Granite, Zinc and Clay Roofing LLC</div>
  </section>
</main>
</body>
</html>
```